tazelbox

I would like a label that would print outside of 24oz cups in Orange. The main ingredient for the cups will be noodles. Just like my lumbix projects, I would accept any funky, creative, funny and well noticed labels. Please keep in mind that we are a Korean food joint.

```html
<!DOCTYPE html>
<html lang="en">
<head>
<meta charset="utf-8">
<title>Tazelbox Noodle Cup Label</title>
<link rel="stylesheet" href="https://fonts.googleapis.com/css2?family=Oswald:wght@700&display=swap">
<style>
  :root {
    --backdrop: #4f6699;
    --label-brown: #2f1516;
    --stripe-red: #8e2a24;
    --stripe-rust: #7a4034;
    --badge-ring: #8b4636;
    --badge-cream: #d2b690;
    --title-cream: #e3c9a2;
    --name-ink: #1a1010;
  }
  html, body {
    margin: 0;
    padding: 0;
    width: 730px;
    height: 1200px;
    overflow: hidden;
    background: var(--backdrop);
  }
  .canvas {
    position: relative;
    width: 730px;
    height: 1200px;
  }
  .cup-label {
    position: absolute;
    left: 65px;
    top: 300px;
    width: 600px;
    height: 600px;
    box-shadow: 6px 8px 14px rgba(20, 25, 50, 0.45);
  }
  .label-field { fill: var(--label-brown); }
  .stripe-red { fill: var(--stripe-red); }
  .stripe-rust { fill: var(--stripe-rust); }
  .badge-ring { fill: var(--badge-ring); }
  .badge-face { fill: var(--badge-cream); }
  .badge-gap { fill: none; stroke: var(--label-brown); stroke-width: 3; }
  .product-title {
    font-family: 'Oswald', sans-serif;
    font-weight: 700;
    font-size: 44px;
    fill: var(--title-cream);
    letter-spacing: 1px;
  }
  .brand-name {
    font-family: 'Oswald', sans-serif;
    font-weight: 700;
    font-size: 66px;
    fill: var(--name-ink);
  }
  .brand-dot { fill: var(--name-ink); }
</style>
</head>
<body>
<div class="canvas">
  <svg class="cup-label" viewBox="0 0 600 600" xmlns="http://www.w3.org/2000/svg">
    <rect class="label-field" x="0" y="0" width="600" height="600"/>

    <!-- title band -->
    <g class="title-band">
      <rect class="stripe-rust" x="0" y="99" width="208" height="4"/>
      <rect class="stripe-red" x="0" y="109" width="208" height="5"/>
      <rect class="stripe-rust" x="0" y="121" width="208" height="4"/>
      <rect class="stripe-rust" x="392" y="99" width="208" height="4"/>
      <rect class="stripe-red" x="392" y="109" width="208" height="5"/>
      <rect class="stripe-rust" x="392" y="121" width="208" height="4"/>
      <text class="product-title" x="300" y="134" text-anchor="middle">NOODLE</text>
    </g>

    <!-- base bars under the badge -->
    <g class="base-bars">
      <rect class="stripe-rust" x="216" y="500" width="6" height="100"/>
      <rect class="stripe-rust" x="236" y="500" width="6" height="100"/>
      <rect class="stripe-red" x="256" y="500" width="6" height="100"/>
      <rect class="stripe-rust" x="276" y="500" width="6" height="100"/>
      <rect class="stripe-rust" x="297" y="500" width="6" height="100"/>
      <rect class="stripe-rust" x="318" y="500" width="6" height="100"/>
      <rect class="stripe-red" x="338" y="500" width="6" height="100"/>
      <rect class="stripe-rust" x="358" y="500" width="6" height="100"/>
      <rect class="stripe-rust" x="376" y="500" width="6" height="100"/>
    </g>

    <!-- badge -->
    <g class="badge">
      <circle class="badge-ring" cx="300" cy="354" r="188"/>
      <circle class="badge-gap" cx="300" cy="354" r="176"/>
      <circle class="badge-face" cx="300" cy="354" r="170"/>
      <circle class="brand-dot" cx="300" cy="282" r="14"/>
      <text class="brand-name" x="300" y="400" text-anchor="middle">Hobmari</text>
    </g>
  </svg>
</div>
</body>
</html>
```